Redesign cement bags for leading cement producer in south east asia

We are from Talvero cement and would like to redesign our bag to relaunch the product line. Our bags are made of high quality PP woven sack. We are one of the leading cement producers and we want our bags to have a Talvero classy look on each visible side when it is loading in a truck or stacking on a pallet.

Thank you for interesting in this project. Good luck.
Updates

Project Deadline Extended Reason: Hi all, I have received requests to extend the deadline. Some of the work requires revising and some of them are still on process. To be fair, I also raise my budget to compensate the time. Thanks all for your participation. Added Sunday, July 10, 2016

Target Market(s)

Construction

Industry/Entity Type

Cement

Requirements
Must have
• You will have to design two bags for two cement grades. 52.5 is of higher grade and 42.5 is of lower grade. Both are similar in design but a distinctive colours to differentiate the two at once. Please look at Reference picture 2 for ideas.
Nice to have
• You do not have to change the original logo but the Talvero cement word font changes are required. There are no restrictions to colours and font but please refrain from using feminine colours. Instructions on rear side of the bags are now included in the scope. Please create new layout and design new user friendly symbols.
Should not have
• Since cement is a dusty product, you need avoid some colours like black as background. The dust need to be less obvious to attract attention. Our previous base colour are shown in below.
• We want a fresh look on our bag, please do not just copy our old design and make small changes. I have attached our competitors' design, please refrain from using their design as well.
• It is recommend to do some research on cement bag sector.

```html
<!DOCTYPE html>
<html lang="en">
<head>
<meta charset="utf-8">
<title>Talvero Cement – Bag Range</title>
<link rel="stylesheet" href="https://fonts.googleapis.com/css2?family=Montserrat:wght@400;600;700;800&display=swap">
<style>
  :root {
    --page-bg: #ffffff;
    --sack-top: #c3c5c9;
    --sack-mid: #e6e7e9;
    --brand-red: #d2232f;

    --blue-light: #3f78ba;
    --blue-mid: #1e4f96;
    --blue-deep: #0d2a66;
    --blue-base: #0c1638;

    --red-light: #cc4650;
    --red-mid: #a81f2a;
    --red-deep: #8c1720;
    --red-base: #4f0a10;

    --white: #ffffff;
  }

  * { box-sizing: border-box; margin: 0; padding: 0; }

  html, body {
    width: 1200px;
    height: 912px;
    overflow: hidden;
    background: var(--page-bg);
    font-family: "Montserrat", Arial, sans-serif;
  }

  .range {
    position: relative;
    width: 1200px;
    height: 912px;
  }

  .sack {
    position: absolute;
    top: 235px;
    width: 328px;
    height: 475px;
  }
  .sack--grade-42 {
    left: 219px;
    --accent: var(--blue-mid);
    --panel-light: var(--blue-light);
    --panel-deep: var(--blue-deep);
    --panel-base: var(--blue-base);
  }
  .sack--grade-52 {
    left: 652px;
    --accent: var(--brand-red);
    --panel-light: var(--red-light);
    --panel-deep: var(--red-deep);
    --panel-base: var(--red-base);
  }

  .sack__body {
    position: absolute;
    inset: 0;
    width: 100%;
    height: 100%;
  }

  .quality-seal {
    position: absolute;
    top: 22px;
    right: 25px;
    width: 40px;
    height: 40px;
    border: 2px solid var(--accent);
    border-radius: 50%;
  }

  .wordmark {
    position: absolute;
    top: 150px;
    left: 0;
    width: 100%;
    text-align: center;
    color: var(--brand-red);
    font-weight: 800;
    line-height: 1;
  }
  .wordmark__name {
    display: block;
    font-size: 40px;
    letter-spacing: 0.5px;
  }
  .wordmark__type {
    display: block;
    margin-top: 8px;
    font-size: 22px;
    letter-spacing: 1.5px;
  }

  .spec {
    position: absolute;
    top: 256px;
    left: 0;
    width: 100%;
    text-align: center;
    color: var(--accent);
  }
  .spec__product {
    font-size: 14px;
    font-weight: 700;
    line-height: 18px;
  }
  .spec__line {
    font-size: 8.5px;
    font-weight: 400;
    line-height: 10px;
  }

  .origin {
    position: absolute;
    top: 392px;
    left: 0;
    width: 100%;
    text-align: center;
    color: var(--white);
  }
  .origin__stars {
    font-size: 9px;
    letter-spacing: 7px;
    padding-left: 7px;
    line-height: 12px;
  }
  .origin__country {
    margin-top: 11px;
    font-size: 10px;
    font-weight: 400;
  }
  .origin__weight {
    margin-top: 8px;
    font-size: 10px;
    font-weight: 700;
  }
</style>
</head>
<body>
<main class="range">

  <section class="sack sack--grade-42" aria-label="Talvero Cement bag, strength class 42.5">
    <svg class="sack__body" viewBox="0 0 328 475" aria-hidden="true">
      <defs>
        <linearGradient id="sackTopBlue" x1="0" y1="0" x2="0" y2="1">
          <stop offset="0" stop-color="var(--sack-top)"/>
          <stop offset="0.6" stop-color="var(--sack-mid)"/>
        </linearGradient>
        <linearGradient id="baseBlue" x1="0" y1="0" x2="0" y2="1">
          <stop offset="0" stop-color="var(--blue-mid)"/>
          <stop offset="1" stop-color="var(--blue-base)"/>
        </linearGradient>
      </defs>
      <rect width="328" height="475" fill="url(#sackTopBlue)"/>
      <polygon points="0,251 164,363 0,475" fill="var(--blue-light)"/>
      <polygon points="328,251 164,363 328,475" fill="var(--blue-deep)"/>
      <polygon points="164,363 328,475 0,475" fill="url(#baseBlue)"/>
    </svg>
    <div class="quality-seal" aria-hidden="true"></div>
    <h2 class="wordmark">
      <span class="wordmark__name">TALVERO</span>
      <span class="wordmark__type">CEMENT</span>
    </h2>
    <div class="spec">
      <p class="spec__product">Portland Cement</p>
      <p class="spec__line">EN 197-1 (2000)</p>
      <p class="spec__line">Strength Class 42.5</p>
    </div>
    <div class="origin">
      <p class="origin__stars">★★★</p>
      <p class="origin__country">Product of Myanmar</p>
      <p class="origin__weight">Net Weight 50kg</p>
    </div>
  </section>

  <section class="sack sack--grade-52" aria-label="Talvero Cement bag, strength class 52.5">
    <svg class="sack__body" viewBox="0 0 328 475" aria-hidden="true">
      <defs>
        <linearGradient id="sackTopRed" x1="0" y1="0" x2="0" y2="1">
          <stop offset="0" stop-color="var(--sack-top)"/>
          <stop offset="0.6" stop-color="var(--sack-mid)"/>
        </linearGradient>
        <linearGradient id="baseRed" x1="0" y1="0" x2="0" y2="1">
          <stop offset="0" stop-color="var(--red-mid)"/>
          <stop offset="1" stop-color="var(--red-base)"/>
        </linearGradient>
      </defs>
      <rect width="328" height="475" fill="url(#sackTopRed)"/>
      <polygon points="0,251 164,363 0,475" fill="var(--red-light)"/>
      <polygon points="328,251 164,363 328,475" fill="var(--red-deep)"/>
      <polygon points="164,363 328,475 0,475" fill="url(#baseRed)"/>
    </svg>
    <div class="quality-seal" aria-hidden="true"></div>
    <h2 class="wordmark">
      <span class="wordmark__name">TALVERO</span>
      <span class="wordmark__type">CEMENT</span>
    </h2>
    <div class="spec">
      <p class="spec__product">Portland Cement</p>
      <p class="spec__line">EN 197-1 (2000)</p>
      <p class="spec__line">Strength Class 52.5</p>
    </div>
    <div class="origin">
      <p class="origin__stars">★★★</p>
      <p class="origin__country">Product of Myanmar</p>
      <p class="origin__weight">Net Weight 50kg</p>
    </div>
  </section>

</main>
</body>
</html>
```